Website Hero Image Redesign Brief
The current hero image appears too busy and lacks the elegance that reflects our brand. We would like to create a new, refined hero image for our real estate company's website.
Requirements:
Clean, elegant, and modern look
Should represent premium real estate sales
Use either our existing images from the website or create a custom design
Focus on sophistication, trust, and exclusivity
Ensure the image works well with overlay text and call-to-action buttons

Goal:
The new hero image should immediately convey professionalism, elegance, and the premium nature of our real estate services, while maintaining a calm and inviting visual impression.

Website: https://www.brunnwaldliegenschaften.example/

```html
<!DOCTYPE html>
<html lang="en">
<head>
<meta charset="utf-8">
<title>Brunnwald Liegenschaften – Hero</title>
<link href="https://fonts.googleapis.com/css2?family=Kumbh+Sans:wght@600;700&family=Poppins:wght@400;600&display=swap" rel="stylesheet">
<style>
  :root {
    --backdrop: #a4a4a4;
    --nav-bg: #ffffff;
    --hero-bg: #efefef;
    --ink: #0b0b0b;
    --brand-green: #2f9e4f;
  }
  html, body {
    margin: 0;
    width: 1200px;
    height: 653px;
    overflow: hidden;
    background: var(--backdrop);
  }
  .site {
    position: absolute;
    left: 57px;
    top: 85px;
    width: 1086px;
    height: 484px;
    background: var(--hero-bg);
    overflow: hidden;
  }
  .main-nav {
    position: absolute;
    left: 0; top: 0;
    width: 100%;
    height: 78px;
    background: var(--nav-bg);
    font-family: "Poppins", sans-serif;
    font-size: 12px;
    color: var(--ink);
  }
  .main-nav a {
    position: absolute;
    top: 32px;
    color: inherit;
    text-decoration: none;
    white-space: nowrap;
  }
  .main-nav a.is-active { font-weight: 600; }
  .hero {
    position: absolute;
    left: 0; top: 78px;
    width: 100%;
    height: 406px;
  }
  .brand-name {
    position: absolute;
    left: 90px;
    top: 22px;
    font-family: "Kumbh Sans", sans-serif;
    font-weight: 600;
    color: var(--brand-green);
    line-height: 1;
  }
  .brand-name .word { display: block; font-size: 62px; letter-spacing: -1px; }
  .brand-name .sub { display: block; font-size: 21px; letter-spacing: 4px; margin-top: 10px; padding-left: 40px; }
  .headline {
    position: absolute;
    left: 88px;
    top: 164px;
    margin: 0;
    font-family: "Kumbh Sans", sans-serif;
    font-weight: 700;
    font-size: 51px;
    line-height: 58px;
    letter-spacing: -0.5px;
    color: var(--ink);
    text-transform: uppercase;
  }
  .tagline {
    position: absolute;
    left: 88px;
    top: 352px;
    margin: 0;
    font-family: "Poppins", sans-serif;
    font-size: 12.5px;
    color: var(--ink);
  }
  .hero-photo {
    position: absolute;
    left: 516px;
    top: 0;
    width: 570px;
    height: 406px;
    background:
      linear-gradient(90deg, var(--hero-bg) 0%, rgba(239,239,239,0) 9%),
      linear-gradient(180deg, #c9d6e2 0%, #e6e0d4 22%, #b98a5a 45%, #7a5634 62%, #4d5a3a 78%, #3a3430 100%);
  }
</style>
</head>
<body>
  <div class="site">
    <nav class="main-nav">
      <a class="is-active" href="#" style="left:168px">HOME PAGE</a>
      <a href="#" style="left:283px">ABOUT US</a>
      <a href="#" style="left:387px">SALE</a>
      <a href="#" style="left:458px">OUR REFERENCE</a>
      <a href="#" style="left:596px">OBJECTS</a>
      <a href="#" style="left:694px">CALL-BACK SERVICE</a>
      <a href="#" style="left:858px">CONTACT</a>
    </nav>
    <section class="hero">
      <div class="brand-name">
        <span class="word">Brunnwald</span>
        <span class="sub">LIEGENSCHAFTEN</span>
      </div>
      <h1 class="headline">Your local<br>real estate<br>professional</h1>
      <p class="tagline">Rooted in Meilen - on the move on Lake Zurich</p>
      <div class="hero-photo" role="img" aria-label="Modern two-storey luxury villa with warm-lit interiors, wooden overhangs, a dark sedan in the driveway and green shrubs at dusk"></div>
    </section>
  </div>
</body>
</html>
```